Fatigued and Overloaded by COVID Messages? We need original illustrations to show that.

Everywhere you look there are messages about COVID. That is leading many people to feel fatigued and overloaded by the messages.

We surveyed U.S. adults March 20th - 24th, 2020 and measured message fatigue, information overload, perceived repetition, and perceived exaggeration. Here is how participants responded:

When it comes to coronavirus . . .
55% feel exhausted by all the messages.
54% feel overloaded by the amount of information.
51% feel that the messages are repetitive.
47% feel like messages exaggerate how bad it is.

In other words, almost half of U.S. adults show signs of message fatigue, information overload, perceived message repetition, and perceived message exaggeration.

We will continue to survey 400 adults every week for the next 16 weeks. Each time we will measure message fatigue, information overload, perceived repetition, and perceived exaggeration. We expect that it will increase over time.

What are we looking for? We need innovative and original illustrations that attempt to communicate these findings. The illustrations would visualize message fatigue, information overload, perceived message repetition, and perceived message exaggeration.

What sort of visual are we looking for? Our preference is for an original illustration (or set of illustrations). Our preference is for creative and powerful illustrations, but we are also open to the creative and well-executed infographics.

We need these images fast . We will award monetary prizes to the 3 best designs. If we like more than that, then we might purchase more (e.g., in past contests, we have purchased as many as 30 designs).

What we will need:
(1) The illustrations must be original and we will need the photoshop and/or illustrator files for all artwork. (By original, we mean that the illustrations are 100% created by you. Our organization requires that we utilize only original illustrated work. We have had issues with free imagery being pirated and reposted as free. We sidestep that issue by just having everything created.)

(2) The illustration should say, somewhere: "Based on a survey of 400 U.S. adults conducted March 20 - 24th, 2020."

(3) We will have almost 4 months worth of data by the time this is done. In other words, the illustrations might be able to help us present that weekly data.

(4) We have conducted other Artvendo projects. It might be helpful to examine designs we liked in the past. For example, here is another COVID project we just finished:

https://jobs.artvendo-example.com/job/5162048

Target Market(s)

U.S. adults

Requirements
Must have
• Original illustrations. Mobile friendly design. People will view this on their smartphones.
Nice to have
• A design that we can use to communicate the data across time.

```html
<!DOCTYPE html>
<html lang="en">
<head>
<meta charset="utf-8">
<title>Message Fatigue Survey Infographic</title>
<link rel="stylesheet" href="https://fonts.googleapis.com/css2?family=Alfa+Slab+One&family=Didact+Gothic&family=Oswald:wght@700&display=swap">
<style>
  :root{
    --red:#ec1c24;
    --blue:#2b82c5;
    --sand:#e6e08a;
    --white:#ffffff;
    --ink:#111111;
    --orange:#f6a12d;
    --orange-dark:#bb5f2a;
    --green:#77b442;
    --green-dark:#4c6e37;
    --magenta:#c8197c;
    --magenta-dark:#7a1c55;
    --blue-dark:#2b3e50;
    --virus-light:#8fd07a;
    --virus-deep:#3aaa5c;
    --slab:"Alfa Slab One", serif;
    --gothic:"Didact Gothic", sans-serif;
    --condensed:"Oswald", sans-serif;
  }
  *{margin:0;padding:0;box-sizing:border-box}
  html,body{width:750px;height:1200px;overflow:hidden;background:var(--white)}
  .poster{position:relative;width:750px;height:1200px;background:var(--white);overflow:hidden}

  .headline-band{position:absolute;left:0;top:36px;width:750px;height:116px;background:var(--red);
    padding:13px 0 0 13px}
  .headline{font-family:var(--slab);font-weight:400;color:var(--white);font-size:24px;line-height:30px;
    text-shadow:1px 2px 2px rgba(0,0,0,.55);white-space:nowrap}

  .survey-badge{position:absolute;left:32px;top:174px;width:90px;height:78px;background:var(--blue);
    border-radius:16px;padding:6px}
  .survey-badge .icon-area{width:100%;height:100%;background:var(--white);border-radius:11px;
    display:flex;align-items:center;justify-content:center}
  .survey-badge .icon-area span{display:block;width:56px;height:44px;border-radius:28px 28px 6px 6px;
    background:linear-gradient(var(--blue),#5aa3d8)}
  .survey-tab{position:absolute;left:122px;top:185px;width:245px;height:56px;background:var(--blue);
    padding:5px 0 0 12px;font-family:var(--slab);font-weight:400;color:var(--white);font-size:19px;line-height:23px;
    text-shadow:1px 1px 2px rgba(0,0,0,.4)}

  .method-box{position:absolute;left:387px;top:185px;width:336px;height:290px;background:var(--blue);
    border-radius:8px;padding:8px 0 0 22px;font-family:var(--gothic);color:var(--white);font-size:25.5px;
    line-height:29.2px;letter-spacing:.7px;white-space:nowrap;text-shadow:1px 1px 2px rgba(0,0,0,.35)}

  .panel-top{position:absolute;left:27px;top:273px;width:344px;height:222px;background:var(--sand);border-radius:10px 10px 0 0}
  .panel-main{position:absolute;left:25px;top:490px;width:696px;height:348px;background:var(--sand);border-radius:0 8px 8px 8px}

  .panel-title{position:absolute;left:52px;top:290px;font-family:var(--slab);font-weight:400;color:var(--red);font-size:25px;line-height:25px}

  .media-illustration{position:absolute;left:67px;top:350px;width:266px;height:158px;border-radius:10px;
    background:radial-gradient(circle at 60% 45%, rgba(236,28,36,.55), rgba(236,28,36,.18) 70%)}
  .virus-decor{position:absolute;border-radius:50%;
    background:radial-gradient(circle at 40% 40%, var(--virus-light), var(--virus-deep))}
  .virus-decor.upper{left:588px;top:400px;width:144px;height:140px;opacity:.92}
  .virus-decor.lower{left:304px;top:846px;width:144px;height:144px}

  .stat{position:absolute;width:312px;height:122px;isolation:isolate}
  .stat .card{position:absolute;left:50px;top:25px;width:258px;height:96px;background:var(--white);
    border-radius:0 0 22px 0;box-shadow:3px 4px 5px rgba(0,0,0,.35);z-index:1}
  .stat svg{position:absolute;left:0;top:0;z-index:2}
  .stat .figure{position:absolute;left:52px;top:4px;font-family:var(--slab);color:var(--white);
    font-size:44px;line-height:50px;text-shadow:2px 2px 2px rgba(0,0,0,.4);z-index:3}
  .stat .label{position:absolute;left:75px;top:67px;font-family:var(--condensed);font-weight:700;
    color:var(--ink);font-size:20.5px;line-height:22px;letter-spacing:-.2px;white-space:nowrap;z-index:3}
  .stat.exhausted{left:46px;top:525px}
  .stat.overloaded{left:387px;top:525px}
  .stat.exaggerated{left:48px;top:684px}
  .stat.repetitive{left:390px;top:684px}

  .people-illustration{position:absolute;left:82px;top:893px;width:553px;height:98px;
    background:linear-gradient(90deg, var(--red) 0 45%, var(--ink) 55% 100%);opacity:.85;border-radius:6px}

  .quote{position:absolute;left:22px;top:1004px;width:710px;height:112px}
  .quote svg{position:absolute;left:0;top:0}
  .quote .mark{position:absolute;font-family:var(--slab);font-size:46px;line-height:46px;color:var(--ink)}
  .quote .mark.open{left:0;top:0}
  .quote .mark.close{right:0;bottom:-14px}
  .quote p{position:absolute;left:41px;top:20px;width:660px;font-family:var(--gothic);color:var(--ink);
    font-size:20.5px;line-height:24.5px;letter-spacing:.75px;white-space:nowrap}

  .footnote-band{position:absolute;left:0;top:1134px;width:750px;height:36px;background:var(--red);
    font-family:var(--gothic);color:var(--white);font-size:20.5px;line-height:36px;text-align:center;
    letter-spacing:.2px;text-shadow:1px 1px 2px rgba(0,0,0,.3);white-space:nowrap}
</style>
</head>
<body>
<main class="poster">

  <header class="headline-band">
    <h1 class="headline">Everywhere you look there are messages about COVID.<br>That is leading many people to feel fatigued and<br>overloaded by the messages.</h1>
  </header>

  <div class="survey-badge"><div class="icon-area" role="img" aria-label="Icon of a confused person holding their head with question marks"><span></span></div></div>
  <div class="survey-tab">Information<br>overload survey</div>

  <div class="panel-top"></div>
  <div class="panel-main"></div>

  <section class="method-box">
    We surveyed U.S. adults<br>March 20th - 24th, 2020<br>and measured message<br>fatigue, information<br>overload, perceived<br>repetition, and perceived<br>exaggeration. Here is<br>how participants<br>&nbsp;responded:
  </section>

  <div class="virus-decor upper" role="img" aria-label="Green coronavirus illustration"></div>

  <h2 class="panel-title">When it comes to<br>coronavirus . . .</h2>
  <div class="media-illustration" role="img" aria-label="Red illustration of a shrugging person surrounded by a virus, radio, newspaper, speech bubbles, laptop, television and phone"></div>

  <div class="stat exhausted">
    <div class="card"></div>
    <svg width="312" height="122" viewBox="0 0 312 122" aria-hidden="true">
      <path d="M0 60 L50 60 L50 121 Z" fill="var(--orange-dark)"/>
      <path d="M0 60 L50 0 L200 0 C192 40 175 60 130 60 L50 60 Z" fill="var(--orange)"/>
    </svg>
    <span class="figure">55%</span>
    <p class="label">Feel exhausted by all<br>the messages.</p>
  </div>

  <div class="stat overloaded">
    <div class="card"></div>
    <svg width="312" height="122" viewBox="0 0 312 122" aria-hidden="true">
      <path d="M0 60 L50 60 L50 121 Z" fill="var(--green-dark)"/>
      <path d="M0 60 L50 0 L195 0 C187 40 170 60 125 60 L50 60 Z" fill="var(--green)"/>
    </svg>
    <span class="figure">54%</span>
    <p class="label">Feel overloaded by<br>the amount&nbsp; of information.</p>
  </div>

  <div class="stat exaggerated">
    <div class="card"></div>
    <svg width="312" height="122" viewBox="0 0 312 122" aria-hidden="true">
      <path d="M0 60 L50 60 L50 121 Z" fill="var(--magenta-dark)"/>
      <path d="M0 60 L50 0 L170 0 C162 40 145 60 100 60 L50 60 Z" fill="var(--magenta)"/>
    </svg>
    <span class="figure">47%</span>
    <p class="label">Feel like messages<br>exaggerated how bad it is.</p>
  </div>

  <div class="stat repetitive">
    <div class="card"></div>
    <svg width="312" height="122" viewBox="0 0 312 122" aria-hidden="true">
      <path d="M0 60 L50 60 L50 121 Z" fill="var(--blue-dark)"/>
      <path d="M0 60 L50 0 L182 0 C174 40 157 60 112 60 L50 60 Z" fill="var(--blue)"/>
    </svg>
    <span class="figure">51%</span>
    <p class="label">Feel that messages are<br>repetitive.</p>
  </div>

  <div class="virus-decor lower" role="img" aria-label="Green coronavirus illustration behind the row of people"></div>
  <div class="people-illustration" role="img" aria-label="Row of ten people: five red figures holding their heads in fatigue and five black standing figures"></div>

  <blockquote class="quote">
    <svg width="710" height="112" viewBox="0 0 710 112" aria-hidden="true">
      <path d="M34 7 L704 7 Q709 7 709 12 L709 92" fill="none" stroke="var(--ink)" stroke-width="3"/>
      <path d="M2 36 L2 96 Q2 108 14 108 L672 108" fill="none" stroke="var(--ink)" stroke-width="3"/>
    </svg>
    <span class="mark open">&ldquo;</span>
    <p>In other words, almost half of U.S. adults show signs of message<br>fatigue, information overload, perceived message repetition,<br>and erceived message exaggeration.</p>
    <span class="mark close">&rdquo;</span>
  </blockquote>

  <footer class="footnote-band">"Based on a survey of 400 U.S. adults conducted March 20 - 24th, 2020."</footer>

</main>
</body>
</html>
```